Poster for List of Company Values

We need a poster to outline our Values which will be displayed in our office as well as posted on our website and other platforms (so need to allow for some flexibly in its application).

File attached outlines what we currently have with design and also our company style guide.

Note that we are looking for a modern, clean look, which still represents our core activities of construction and environmental services.

You can also reference our website here:

https://corvellaworks.com.au/

Happy to answer any questions you might have.

Thanks for your interest,
Rhys

Target Market(s)

Internal and External clients

Industry/Entity Type

Construction, water and recycling

Font styles to use
Sans Serif

Requirements
Must have
• All values on the one page. Graphic to represent each value. Also needs to use company logo
Nice to have
• Preference for poster to be orientated in landscape
Should not have
• Do not follow example provided, this is only to demonstrate what we have to date and also the text required

```html
<!DOCTYPE html>
<html lang="en">
<head>
<meta charset="utf-8">
<title>Core Values – Corvella Works</title>
<link rel="stylesheet" href="https://fonts.googleapis.com/css2?family=Fira+Sans:ital,wght@0,500;0,700;0,800;1,400;1,500&display=swap">
<style>
  :root {
    --blue: #1a3fd0;
    --blue-deep: #1434c4;
    --green: #4af004;
    --white: #ffffff;
    --navy: #1f2b5c;
    --rule-light: #c9d3f2;
  }
  * { margin: 0; padding: 0; box-sizing: border-box; }
  html, body {
    width: 939px; height: 1200px; overflow: hidden;
    background: var(--white);
    font-family: "Fira Sans", Arial, sans-serif;
  }
  .poster {
    position: relative; width: 939px; height: 1200px;
    background: var(--blue-deep); overflow: hidden;
  }
  .poster__accent { position: absolute; inset: 0; }
  .poster__sheet {
    position: absolute; left: 27px; top: 27px; right: 27px; bottom: 27px;
    background: var(--white);
  }
  .poster__title {
    position: absolute; left: 0; right: 0; top: 78px;
    text-align: center; color: var(--blue-deep);
    font-weight: 700; font-size: 100px; letter-spacing: 3px; line-height: 1;
  }
  .poster__rule {
    position: absolute; left: 176px; width: 592px; top: 196px; height: 4px;
    background: linear-gradient(90deg, var(--white), var(--rule-light) 25%, var(--blue) 50%, var(--rule-light) 75%, var(--white));
  }
  .value {
    position: absolute; width: 416px; height: 259px;
    color: var(--white); padding: 14px 14px;
  }
  .value--blue { background: var(--blue); }
  .value--green { background: var(--green); }
  .value--left { left: 46px; }
  .value--right { left: 477px; }
  .value--row1 { top: 235px; }
  .value--row2 { top: 509px; }
  .value--row3 { top: 782px; height: 261px; }
  .value__lead { font-style: italic; font-weight: 400; font-size: 22px; line-height: 1.1; }
  .value__name { font-weight: 700; font-size: 50px; line-height: 1.05; letter-spacing: 1px; margin-top: -2px; }
  .value__text {
    font-style: italic; font-weight: 400; font-size: 23.5px; line-height: 36px;
    margin-top: 14px; width: 300px;
  }
  .value__icon {
    position: absolute; top: 12px; right: 18px; width: 84px; height: 84px;
    border-radius: 50%; background: rgba(255,255,255,0.85);
  }
  .brand {
    position: absolute; top: 1076px; left: 0; right: 0;
    display: flex; justify-content: center; align-items: center; gap: 12px;
  }
  .brand__mark { width: 44px; height: 44px; background: var(--blue-deep); }
  .brand__name {
    color: var(--navy); font-weight: 700; font-size: 28px; line-height: 1.05;
  }
</style>
</head>
<body>
<main class="poster">
  <svg class="poster__accent" width="939" height="1200" viewBox="0 0 939 1200" aria-hidden="true">
    <polygon points="0,900 939,1020 939,1200 0,1200" fill="#4af004"/>
  </svg>
  <div class="poster__sheet"></div>

  <h1 class="poster__title">CORE VALUES</h1>
  <div class="poster__rule"></div>

  <section class="value value--blue value--left value--row1">
    <p class="value__lead">be</p>
    <h2 class="value__name">LOYAL</h2>
    <p class="value__text">We take care of our own and provide opportunities to listen and support each other.</p>
    <div class="value__icon" role="img" aria-label="Icon of a person inside a circle"></div>
  </section>

  <section class="value value--green value--right value--row1">
    <p class="value__lead">show</p>
    <h2 class="value__name">INITIATIVE</h2>
    <p class="value__text">We celebrate and recognize our own and encourage forward thinking.</p>
    <div class="value__icon" role="img" aria-label="Icon of a head profile with a gear and lightbulb"></div>
  </section>

  <section class="value value--green value--left value--row2">
    <p class="value__lead">think</p>
    <h2 class="value__name">TEAM</h2>
    <p class="value__text" style="width:330px">We communicate effectively and work as a team by helping and supporting each other.</p>
    <div class="value__icon" role="img" aria-label="Icon of a group of people"></div>
  </section>

  <section class="value value--blue value--right value--row2">
    <p class="value__lead">show</p>
    <h2 class="value__name">RESPECT</h2>
    <p class="value__text" style="width:200px">We value the diversity and opinions of all.</p>
    <div class="value__icon" role="img" aria-label="Icon of two people shaking hands"></div>
  </section>

  <section class="value value--blue value--left value--row3">
    <p class="value__lead">be</p>
    <h2 class="value__name">HONEST</h2>
    <p class="value__text" style="width:370px">We are clear and open with each other, and provide an approachable and friendly environment.</p>
    <div class="value__icon" role="img" aria-label="Icon of a person with hand on heart"></div>
  </section>

  <section class="value value--green value--right value--row3">
    <p class="value__lead">be</p>
    <h2 class="value__name">POSITIVE</h2>
    <p class="value__text" style="width:360px">We are solutions focused and encourage a positive attitude turning a negative into a positive.</p>
    <div class="value__icon" role="img" aria-label="Icon of a person giving a thumbs up"></div>
  </section>

  <footer class="brand">
    <span class="brand__mark" aria-hidden="true"></span>
    <span class="brand__name">CORVELLA<br>Works</span>
  </footer>
</main>
</body>
</html>
```